Finally a Vodka produced for women ! (Label Design)

We are a small distillery based in Melbourne, Australia and we need a Vodka label design solution that will appeal to women aged 30-50 years and radiate luxury. Full Details are in a design brief attached. We thank you in advance.

Target Market(s)

Affluent females 30-50 years.

Industry/Entity Type

Spirits/Alcohol

Requirements
Must have
• Be clear this is a luxury Vodka.
Nice to have
• Elegance.

```html
<!DOCTYPE html>
<html lang="en">
<head>
<meta charset="utf-8">
<title>Silver Wren Premium Vodka – Label</title>
<link rel="stylesheet" href="https://fonts.googleapis.com/css2?family=Cinzel:wght@500;700&family=Cormorant+Garamond:wght@500&family=Playball&display=swap">
<style>
  :root {
    --page: #ffffff;
    --label-pink: #cc9fd8;
    --glass-mauve: #6e5880;
    --glass-deep: #55445f;
    --glass-shadow: #3f3146;
    --highlight-pink: #fbcbfd;
    --highlight-white: #ffffff;
    --silver-dark: #7f8b8c;
    --silver-light: #f6f7f7;
    --neck-black: #0b0c0b;
    --ink: #111111;
  }
  html, body {
    margin: 0;
    padding: 0;
    overflow: hidden;
    background: var(--page);
  }
  .canvas {
    position: relative;
    width: 848px;
    height: 1200px;
    overflow: hidden;
    background: var(--page);
  }
  .bottle {
    position: absolute;
    inset: 0;
    width: 848px;
    height: 1200px;
  }
  .text {
    position: absolute;
    left: 0;
    width: 848px;
    text-align: center;
    margin: 0;
    color: var(--ink);
  }
  .abv {
    top: 183px;
    left: 364px;
    width: 127px;
    font-family: "Cinzel", serif;
    font-weight: 500;
    font-size: 14px;
    color: #d8d8d8;
    letter-spacing: 0.5px;
  }
  .brand {
    top: 384px;
    left: 331px;
    width: 200px;
    font-family: "Cinzel", serif;
    font-weight: 700;
    font-size: 22px;
    line-height: 24px;
    letter-spacing: 8px;
  }
  .brand .brand-sub {
    display: block;
    font-size: 11px;
    letter-spacing: 6px;
    line-height: 16px;
  }
  .product-name {
    top: 522px;
    left: 8px;
    font-family: "Playball", cursive;
    font-size: 104px;
    line-height: 1;
  }
  .grade {
    top: 636px;
    left: 382px;
    width: 170px;
    text-align: left;
    font-family: "Cormorant Garamond", serif;
    font-weight: 500;
    font-size: 24px;
    letter-spacing: 10px;
  }
  .feature {
    top: 915px;
    left: 4px;
    font-family: "Cinzel", serif;
    font-weight: 700;
    font-size: 23px;
  }
  .volume {
    top: 984px;
    font-family: "Cinzel", serif;
    font-weight: 700;
    font-size: 36px;
  }
</style>
</head>
<body>
<div class="canvas">
  <svg class="bottle" viewBox="0 0 848 1200" xmlns="http://www.w3.org/2000/svg">
    <defs>
      <linearGradient id="silver" x1="0" x2="1" y1="0" y2="0">
        <stop offset="0" stop-color="#dfe2e2"/>
        <stop offset="0.15" stop-color="var(--silver-dark)"/>
        <stop offset="0.35" stop-color="#e6e9e9"/>
        <stop offset="0.55" stop-color="var(--silver-light)"/>
        <stop offset="0.8" stop-color="#b3bbbb"/>
        <stop offset="0.92" stop-color="var(--silver-dark)"/>
        <stop offset="1" stop-color="#c9cfcf"/>
      </linearGradient>
      <linearGradient id="map-silver" x1="0" x2="1" y1="0" y2="0">
        <stop offset="0" stop-color="#c2c8c8"/>
        <stop offset="0.5" stop-color="#eef0f0"/>
        <stop offset="1" stop-color="#fbfbfb"/>
      </linearGradient>
    </defs>

    <!-- cap and collar -->
    <rect class="cap" x="357" y="55" width="140" height="43" rx="3" fill="var(--label-pink)"/>
    <rect class="collar" x="359" y="100" width="136" height="53" rx="3" fill="url(#silver)"/>
    <rect class="neck-band" x="364" y="153" width="127" height="82" fill="var(--neck-black)"/>

    <!-- glass body -->
    <polygon class="glass-body" points="359,233 491,233 518,255 704,895 614,1088 241,1088 152,895 338,255" fill="var(--glass-mauve)"/>
    <polygon class="glass-base" points="172,900 285,970 396,1044 459,1044 572,970 683,900 704,895 614,1088 241,1088 152,895" fill="var(--glass-deep)"/>
    <polygon class="glass-base-shade" points="152,895 172,900 285,1088 241,1088" fill="var(--glass-shadow)"/>

    <!-- front label -->
    <polygon class="label-face" points="289,425 566,425 683,895 572,970 285,970 172,895" fill="var(--label-pink)"/>
    <polygon class="label-highlight-left" points="289,425 308,436 182,880 172,895" fill="var(--highlight-pink)"/>
    <polygon class="label-highlight-right" points="508,460 528,452 695,880 684,888" fill="var(--highlight-white)"/>

    <!-- silver shoulder -->
    <polygon class="shoulder-foil" points="359,233 491,233 518,255 566,425 427,510 289,425 338,255" fill="url(#silver)"/>

    <!-- emblem area: map with rose -->
    <rect class="emblem" x="280" y="677" width="308" height="234" rx="40" fill="url(#map-silver)" role="img" aria-label="Silver outline map of Australia with a pink rose illustration"/>

    <!-- volume band -->
    <polygon class="volume-foil" points="285,970 572,970 459,1044 396,1044" fill="url(#silver)"/>
  </svg>

  <p class="text abv">40% ALC/VOL</p>
  <p class="text brand">SILVER<br>WREN<span class="brand-sub">DISTILLERY</span></p>
  <h1 class="text product-name">Vodka</h1>
  <p class="text grade">PREMIUM</p>
  <p class="text feature">Rose Quartz Filtered</p>
  <p class="text volume">700ml</p>
</div>
</body>
</html>
```